Design a new jar label for a successful company

We are seeking a fresh label design that will be applied to a glass jar containing our high quality dried flower. We are a company based out of Washington State and we mainly sell dried herbs and oil extracts. The brand is "Copper Hollow" and the product is "Copper Hollow - Handcrafted Flower". I'd like to start with Black/Chrome as the color scheme, but we are open to other suggestions (for example dark purple instead of black). This will be professionally printed on a glossy label and the chrome or auxiliary colors can/will printed with a metallic foil.

BASIC REQUIREMENTS:

Size: 1.25" H x 2.5" L

Colors: Black and chrome. Preferably use a black background and make the logo/text chrome. Open to suggestions.

Margin: Please do not place any text within 1/16" around the edges to allow for deviation during die cutting process.

Logo: Use the Copper Hollow shield as the center piece.

Required text: State "Handcrafted Flower" somewhere below the logo. Discretely place "QTRNE.COM" somewhere on the label.

Requirements
Must have
• The following warning most appear on the label. Please see attached graphic and also be sure to include the "21 and over" circular icon if possible:
• "Warning: This product has intoxicating effects and may be habit forming. Marijuana can impair concentration, coordination, and judgement. Do not operate a vehicle or machinery under the influence of this drug. There may be health risks associated with consumption of this product."
• "For use only by adults twenty-one and older. Keep out of reach of children."
• Note: You can use the circular 21 and over warning shown in the attached example instead of typing the text out.
Nice to have
• Fonts used - Dorian Pelko - FestivoLettersNo1.otf (This is the logo font.)
• Minion Pro - this is our standard copy font

```html
<!DOCTYPE html>
<html lang="en">
<head>
<meta charset="utf-8">
<title>Copper Hollow – Jar Label</title>
<link rel="stylesheet" href="https://fonts.googleapis.com/css2?family=Bebas+Neue&family=Figtree:wght@400;700&family=Oswald:wght@500;600&display=swap">
<style>
  :root {
    --page-bg: #dcdcdc;
    --label-black: #0a080c;
    --ink-white: #ffffff;
    --violet: #7a3cf2;
    --violet-deep: #4a12b8;
    --violet-glow: #8c3cff;
  }
  * { margin: 0; padding: 0; box-sizing: border-box; }
  html, body {
    width: 1200px;
    height: 900px;
    overflow: hidden;
    background: var(--page-bg);
  }
  .label {
    position: absolute;
    left: 80px;
    top: 190px;
    width: 1040px;
    height: 520px;
    background: var(--label-black);
    overflow: hidden;
    color: var(--ink-white);
  }
  .flower-photo {
    position: absolute;
    left: 110px;
    top: 50px;
    width: 700px;
    height: 480px;
    background:
      radial-gradient(ellipse 34% 40% at 50% 60%, rgba(90, 22, 200, 0.85), rgba(74, 18, 184, 0.35) 60%, transparent 100%),
      radial-gradient(ellipse 50% 30% at 50% 62%, rgba(140, 60, 255, 0.45), transparent 100%),
      radial-gradient(ellipse 18% 30% at 52% 25%, rgba(122, 60, 242, 0.55), transparent 100%);
  }
  .shield-emblem {
    position: absolute;
    left: 389px;
    top: 112px;
    width: 230px;
    height: 98px;
    background: radial-gradient(ellipse 50% 45% at 50% 70%, rgba(255, 255, 255, 0.55), rgba(255, 255, 255, 0.12) 70%, transparent 100%);
  }
  .brand-name {
    position: absolute;
    left: 0;
    width: 1020px;
    top: 228px;
    text-align: center;
    font-family: "Bebas Neue", "Oswald", sans-serif;
    font-weight: 400;
    font-size: 93px;
    line-height: 92px;
    letter-spacing: 2px;
    color: var(--ink-white);
  }
  .product-line {
    position: absolute;
    left: 0;
    width: 1020px;
    top: 434px;
    text-align: center;
    font-family: "Oswald", sans-serif;
    font-weight: 600;
    font-size: 18px;
    line-height: 26px;
    letter-spacing: 5px;
    text-transform: uppercase;
    color: var(--ink-white);
  }
  .site-url {
    position: absolute;
    left: 23px;
    top: 471px;
    font-family: "Oswald", sans-serif;
    font-weight: 600;
    font-size: 15px;
    letter-spacing: 0.3px;
    color: var(--ink-white);
  }
  .warning {
    position: absolute;
    right: 34px;
    top: 55px;
    width: 200px;
    text-align: right;
    font-family: "Figtree", sans-serif;
    font-size: 10.5px;
    line-height: 17.4px;
    color: var(--ink-white);
  }
  .warning strong { font-weight: 700; }
  .warning .children {
    margin-top: 10px;
    font-weight: 700;
  }
  .age-badge {
    position: absolute;
    left: 924px;
    top: 408px;
    width: 84px;
    height: 84px;
  }
  .age-badge text {
    font-family: "Figtree", sans-serif;
    font-weight: 700;
    fill: var(--violet);
  }
</style>
</head>
<body>
  <main class="label">
    <div class="flower-photo" role="img" aria-label="Close-up photograph of a purple-tinted cannabis flower bud"></div>

    <div class="shield-emblem" role="img" aria-label="Copper Hollow shield emblem"></div>

    <h1 class="brand-name">Copper<br>Hollow</h1>

    <p class="product-line">Handcrafted Flower</p>

    <p class="site-url">QTRNE.COM</p>

    <div class="warning">
      <p><strong>Warning:</strong> This product has intoxicating effects and may be habit forming. Marijuana can impair concentration, coordination, and judgement. Do not operate a vehicle or machinery under the influence of this drug. There may be health risks associated with consumption of this product.</p>
      <p class="children">Keep out of reach of children.</p>
    </div>

    <svg class="age-badge" viewBox="0 0 84 84" role="img" aria-label="For use only by adults 21 or older">
      <defs>
        <path id="badge-ring" d="M42,42 m-33,0 a33,33 0 1,1 66,0 a33,33 0 1,1 -66,0"/>
      </defs>
      <text font-size="8.6" letter-spacing="0.4">
        <textPath href="#badge-ring" startOffset="0">FOR USE ONLY BY ADULTS 21 OR OLDER.</textPath>
      </text>
      <text x="42" y="54" text-anchor="middle" font-size="33">21</text>
    </svg>
  </main>
</body>
</html>
```